Web Design Project

The project is about a web design for a brand new dental clinic: Orla Dental Clinic. The dental clinic is located in NSW and the target market is population of all ages (although specialised pediatric dentistry will not be offered at the clinic)
The design is to be:
• Modern
• Professional
• Simple but very attractive
• Logically organised
• Clean
• Fresh
• Engaging
• Friendly
• Creative
Design is to have:
• The dental clinic logo to be shown at the top of every page
• The address and phone number also to be shown at the top of every page
• A link for an online appointment on all pages
• Easy to navigate pages
• Tabs which are easy to identify and read. The tabs are also to be shown at the bottom of each page.
• With drop down menus to be displayed as you scroll along tabs
• Text that is easy to read
• A good use of the colour
• Photos of people smiling. These photos are to be very selective, meaningful and fresh as they play an important role suggesting excellent dental health.
• Short messages
The design is NOT to have:
- Similarities with any other dental clinic (the web design should be authentic and genuine)
- Photos of teeth or smiles on their own or dentists practising the dental work on patients
The site is to include the following pages:
• HOME – this is the welcome page. This page will contain a thank you message and an invitation to visit the dental clinic. It will also have a follow us on chatterbox and quillpost and an area to display testimonials.
• ABOUT US – this page will contain a summary of who we are and the business mission.
• OUR SERVICES – this page is to include a list of the different dental treatments that will be provided at the clinic. Each treatment will have a link to a small window containing a brief description of what the treatment is. This page will also have a section for guarantees on dental work.
• OUR TEAM – this page will have a photo of the professionals that will be working at the clinic and which includes dentists, dental hygienist, dental assistant and administrative assistant.
• OUR TECHNOLOGY – this page will show equipment and technology that we have available at the clinic.
• GALLERY – on this page we will display the ‘before’ and ‘after’ of different treatments conducted, photos of the clinic, etc.
• SPECIAL OFFERS – this page is to contain a list of the discounts available. This page is to include an area to display special offers that will be offered in addition to standard discounts. This page must also include an option for the client to subscribe to our special offers/updates via email. It must also include payment options. It must also include a voucher design which can be printed for discounts.
• LATEST NEWS – this page will include information on latest technical advances on the dental field and may also have links to other documents
• CONTACT US – this page must include:
o the name of the clinic, full address, phone number, fax number, email address
o the business hours
o a location map – link to roamchart
o an option under: Using public transport? Plan your trip at: www.transitplanr.example.au
o an option under: Driving your vehicle? Obtain trip directions at: www.routeduo.example.au
o parking availability
o a ‘print this page’ option
o a photo of the premises for easy identification of the location
• ONLINE APPOINTMENTS – this page must include cells for:
o name
o surname
o mobile number, alternative phone number, email address
o best contact: mobile/alternative number/email
o preferred date and preferred time of the appointment
o are you an existing client/a new patient?
o describe any special needs you may have (e.g. wheelchair access, other)
o how did you hear from us
• TESTIMONIALS/FEEDBACK
I can upload the logo design file upon your request (please specify the type of file required).
In addition to the web design, please indicate if you can undertake the coding for this webpage and if so, please provide a quote.
Updates
Hi there,
Thanks for your interest in this project.
I have uploaded the logo in .jpg, .ai and .eps files. Please feel free to let me know if further information is required.
Best regards,
Marisol

```html
<!DOCTYPE html>
<html lang="en">
<head>
<meta charset="utf-8">
<title>Technology – Orla Dental Clinic</title>
<link rel="stylesheet" href="https://fonts.googleapis.com/css2?family=Arimo:wght@400;700&family=Open+Sans:wght@400;600&display=swap">
<style>
:root{
  --ink:#222;
  --body:#4a4a4a;
  --blue:#2a8fd0;
  --blue-dark:#1f6ea8;
  --link:#1d5f94;
  --green:#7cc325;
  --sky:#e3f3fb;
  --panel:#efefef;
  --line:#bfe1f2;
}
*{margin:0;padding:0;box-sizing:border-box}
html,body{width:1200px;height:1166px;overflow:hidden}
body{position:relative;font-family:"Open Sans",sans-serif;color:var(--body);
  background:linear-gradient(#0a0a0a 0,#0a0a0a 228px,#2b94d6 228px,#8ccbee 380px,#fff 540px,#fff 975px)}
.abs{position:absolute}
.topbar{left:0;top:0;width:1200px;height:140px;background:linear-gradient(#3a3a3a,#151515);border-bottom:1px solid #000}
.logo{left:146px;top:22px;width:250px;height:105px}
.logo .mark{position:absolute;left:0;top:6px;width:62px;height:62px;border-radius:50%;background:var(--blue)}
.logo .name{position:absolute;left:74px;top:8px;font:700 30px/1 Arimo,sans-serif;color:var(--blue)}
.logo .name small{display:block;font-size:20px;margin-top:6px;letter-spacing:2px}
.logo .tag{position:absolute;left:92px;top:92px;font:600 9px/1 "Open Sans",sans-serif;color:#fff;white-space:nowrap}
.contact{right:139px;top:21px;text-align:right;font-size:12.5px;line-height:14px;color:#4cb6f0;white-space:nowrap}
.email{right:139px;top:68px;font-size:20px;color:#fff}
.appt{right:139px;top:102px;font-size:14px;color:#c7f04a;display:flex;align-items:center;gap:8px}
.nav{left:139px;top:140px;width:922px;height:53px;display:flex;align-items:center;justify-content:space-between;padding:0 8px 0 12px;list-style:none}
.nav li{font:700 13px Arimo,sans-serif;color:#fff;padding:5px 8px;border-radius:2px}
.nav li.active{background:var(--green);color:#222}
.page{left:139px;top:193px;width:922px;height:782px;background:#fff}
h1{left:160px;top:222px;font:400 26px Arimo,sans-serif;color:var(--ink)}
h1 .b{color:var(--blue)} h1 .g{color:var(--green)}
.rule{left:159px;top:262px;width:629px;height:1px;background:#c8c8c8}
p.copy{width:622px;left:159px;font-size:10.6px;line-height:16px}
h2{left:157px;font:700 22px Arimo,sans-serif;color:var(--blue)}
.facts{left:157px;top:452px;width:627px;height:187px;background:var(--panel);list-style:none;padding:8px 0 0 24px}
.facts li{font:14px/24px Arimo,sans-serif;color:var(--link);position:relative}
.facts li::before{content:"";position:absolute;left:-11px;top:8px;border:4px solid transparent;border-left:5px solid var(--link)}
.device{left:235px;top:815px;width:392px;height:65px;border-radius:32px 10px 30px 32px;background:linear-gradient(#d9dde0,#6d7276 60%,#2a2a2a)}
.side{left:803px;top:224px;width:241px;height:710px;background:var(--sky)}
.box-head{left:816px;width:215px;height:36px;color:#fff;font:400 18px/36px Arimo,sans-serif;padding-left:10px}
.box-head::after{content:"";position:absolute;left:14px;bottom:-7px;border:7px solid transparent;border-bottom:0;border-top-color:inherit}
.hours-head{top:239px;background:var(--blue);border-color:var(--blue)}
.forms-head{top:470px;background:var(--green);border-color:var(--green)}
.hours{left:816px;top:291px;width:215px;font:12.5px Arimo,sans-serif;color:#111}
.hours div{display:flex;justify-content:space-between;height:32px;line-height:32px;padding:0 15px 0 13px;border-bottom:1px solid var(--line)}
.hours div:last-child{border:0}
.hours span+span{color:var(--blue-dark)}
.forms-copy{left:818px;top:524px;width:215px;font-size:10.5px;line-height:14px}
.btn-dl{left:817px;top:566px;width:112px;height:26px;border-radius:4px;background:linear-gradient(#444,#111);color:#fff;font:12.5px/26px Arimo,sans-serif;text-align:center}
.portrait{left:817px;top:621px;width:213px;height:158px;background:linear-gradient(135deg,#5a4a40,#c49a83 55%,#2a2a2a)}
.social{left:816px;top:805px;width:215px;height:103px;background:#fff;border:1px solid #cfe3ee}
.sbtn{left:828px;width:191px;height:33px;border-radius:3px;color:#fff;font:700 12.5px/33px Arimo,sans-serif;padding-left:10px;display:flex;align-items:center;gap:6px;white-space:nowrap}
.sbtn.q{top:818px;background:linear-gradient(#5fc3ee,#238fc6)}
.sbtn.c{top:861px;background:linear-gradient(#6a86c4,#34518f)}
.sbtn .dot{width:18px;height:18px;border-radius:50%;background:#fff;flex:none}
.footer{left:0;top:975px;width:1200px;height:191px;border-top:4px solid var(--blue);background:linear-gradient(#b5e07a,#78b534 50%,#4e8e18)}
.footer-inner{left:139px;top:979px;width:922px;height:187px;background:linear-gradient(#a9db66,#6ea925 60%,#4d8a16)}
.fnav{left:139px;top:1011px;width:922px;text-align:center;font:700 11px Arimo,sans-serif;color:#1f3e0a;word-spacing:2px}
.legal{left:139px;top:1049px;width:922px;text-align:center;font:11px/16px Arimo,sans-serif;color:#fff}
.follow{left:139px;top:1102px;width:922px;text-align:center;font:14px/30px Arimo,sans-serif;color:#fff}
</style>
</head>
<body>
<div class="abs topbar"></div>
<div class="abs logo">
  <div class="mark"></div>
  <div class="name">Orla<small>Dental Clinic</small></div>
  <div class="tag">Care | Comfort | Confidence</div>
</div>
<div class="abs contact">42 Tallow Street, Bramley, NSW 12480<br>Telephone : 555-ORLA-DNT / 555-014-2290 / 555-017-3381<br>Fax : 555-019-4472</div>
<div class="abs email">info@orladental.example</div>
<div class="abs appt">
  <svg width="24" height="24" viewBox="0 0 24 24" aria-hidden="true"><rect x="2" y="4" width="20" height="18" rx="2" fill="#fff" stroke="#d9542b" stroke-width="2"/><rect x="2" y="4" width="20" height="5" fill="#d9542b"/><text x="12" y="19" font-size="9" text-anchor="middle" fill="#333" font-family="Arial">15</text></svg>
  Click here for online appointments
</div>
<ul class="abs nav">
  <li>HOME</li><li>ABOUT US</li><li>SERVICES</li><li>OUR TEAM</li><li class="active">TECHNOLOGY</li><li>GALLERY</li><li>SPECIAL OFFERS</li><li>NEWS</li><li>TESTIMONIALS</li><li>CONTACT US</li>
</ul>

<main class="abs page"></main>
<h1 class="abs">Dental Technology at <span class="b">Orla</span> <span class="g">Dental</span> <span class="b">Clinic</span></h1>
<div class="abs rule"></div>
<p class="abs copy" style="top:283px">Lorem Ipsum is simply dummy text of the printing and typesetting industry. Lorem Ipsum has been the industry's standards dummy text ever since the 1500s, when an unknown printer took a galley of type and scrambled it to make type the specimen book. It has survived not only five centuries, but also the leap into electronic.</p>

<h2 class="abs" style="top:352px">01. Digital X-rays</h2>
<p class="abs copy" style="top:387px">There are many variations of passages of Lorem Ipsum available, but the majority have suffered alteration in some form and for injected humour, or randomised words which do look even slightly believable. All the Lorem Ipsum of the generators on the Internet tend to repeat predefined chunks as necessary, making this the first true generator.</p>
<ul class="abs facts">
  <li>Small areas of decay between teeth or below existing restorations (fillings)</li>
  <li>Deep cavities</li>
  <li>Infections that can develop in the jaw bones</li>
  <li>Deep gum disease</li>
  <li>Abscesses or cysts</li>
  <li>Developmental abnormalities</li>
  <li>Some types of tumors</li>
</ul>

<h2 class="abs" style="top:660px">02. Intraoral Camera</h2>
<p class="abs copy" style="top:695px">There are many variations of passages of Lorem Ipsum available, but the majority have suffered alteration in some form and for injected humour, or randomised words which do look even slightly believable. All the Lorem Ipsum of the generators on the Internet tend to repeat predefined chunks as necessary, making this the first true generator.</p>

<h2 class="abs" style="top:763px">03. Laser Cavity Detection</h2>
<div class="abs device" role="img" aria-label="Handheld laser cavity detection device"></div>
<p class="abs copy" style="top:894px">There are many variations of passages of Lorem Ipsum available, but the majority have suffered alteration in some form and for injected humour, or randomised words which do look even slightly believable.</p>

<aside class="abs side"></aside>
<div class="abs box-head hours-head">Clinic Hours</div>
<div class="abs hours">
  <div><span>Monday:</span><span>7am - 7pm</span></div>
  <div><span>Tuesday:</span><span>7am - 7pm</span></div>
  <div><span>Wednesday:</span><span>7am - 7pm</span></div>
  <div><span>Thursday:</span><span>7am - 7pm</span></div>
  <div><span>Friday:</span><span>7am - 2pm</span></div>
</div>
<div class="abs box-head forms-head">New Patient Forms</div>
<p class="abs forms-copy">For your convenience, we invite all the new patients to download.</p>
<div class="abs btn-dl">Download Form</div>
<div class="abs portrait" role="img" aria-label="Photo of a smiling young woman patient"></div>
<div class="abs social"></div>
<div class="abs sbtn q">FOLLOW US ON quillpost</div>
<div class="abs sbtn c"><span class="dot"></span>FIND US ON chatterbox</div>

<footer class="abs footer"></footer>
<div class="abs footer-inner"></div>
<div class="abs fnav">HOME - ABOUT US - SERVICES - OUR TEAM - TECHNOLOGY - GALLERY - SPECIAL OFFERS - NEWS - TESTIMONIALS - CONTACT US</div>
<div class="abs legal">© Copyright 2012 Orla Dental Clinic. All Rights Reserved<br>Website Design &amp; Developed | SEO PPC Services: www.pixelgrove.example</div>
<div class="abs follow">Follow us on - chatterbox · quillpost</div>
</body>
</html>
```